Rapidly growing regional logistics company looking for a modern clean website design.

We need a website for a 5 year old company based in New England.
We offer a complete logistics solution. With services dedicated to the changing economic environment. Services to our customers include, same day delivery, trucking and van service, warehouse & storage, pool distribution, and B2B installations.
We've implemented leading technology along the way, that provides visibility, accountability, up to the minute tracking, and project management.
Our goal to be known in the industry we service as an excellent provider of time-critical services and dependability.
Independently of the services we offer, our customers know that they can count on a true partner.

Target Market(s)

B2B, including printers, retail, manufacturers, wholesalers, electronics, any company that needs product delivered or warehoused

Industry/Entity Type

Logistics

Coding

Coded - Design and coding required

Number of Pages Required

5+ page

Font styles to use
Sans Serif

Colors
0255a3

Requirements
Must have
• Clean, modern design, limited clutter. Limited tabs, preferred everything on 1st screen roll down to see info

```html
<!DOCTYPE html>
<html lang="en">
<head>
<meta charset="utf-8">
<title>Northgate Logistics</title>
<link href="https://fonts.googleapis.com/css2?family=Open+Sans:wght@400;600;700&family=Roboto:wght@400;500;700&display=swap" rel="stylesheet">
<style>
:root{
  --blue:#4d72b8;
  --blue-dark:#2f58a3;
  --blue-deep:#0255a3;
  --blue-soft:#6b8cc9;
  --ink:#222;
  --muted:#9a9a9a;
  --grey-bg:#f2f3f5;
  --panel:#3b3d45;
  --foot:#3a3a3a;
  --foot-dark:#2a2a2a;
  --foot-text:#f2f2f2;
  --white:#fff;
}
*{box-sizing:border-box;margin:0;padding:0}
html,body{width:1200px;height:3600px;overflow:hidden}
body{position:relative;font-family:"Open Sans",Arial,sans-serif;color:var(--ink);background:var(--white)}
.abs{position:absolute}

/* header */
.topbar{left:300px;top:0;width:900px;height:43px;background:var(--blue);border-bottom-left-radius:40px;color:#fff;font-size:17px;display:flex;justify-content:flex-end;align-items:center;gap:36px;padding-right:90px;white-space:nowrap}
.topbar span{display:flex;align-items:center;gap:10px}
.brand{left:80px;top:10px;width:180px;text-align:center}
.brand-dot{width:64px;height:64px;border-radius:50%;background:var(--blue);margin:0 auto 6px}
.brand-name{font-family:"Roboto",Arial,sans-serif;font-weight:500;font-size:24px;color:var(--blue-dark);letter-spacing:1px;line-height:1}
.nav{left:330px;top:72px;display:flex;gap:34px;font-family:"Roboto",Arial,sans-serif;font-weight:500;font-size:19px;white-space:nowrap}
.nav .active{position:relative}
.nav .active::after{content:"";position:absolute;left:-12px;right:-12px;top:40px;height:5px;background:var(--blue)}
.search{left:1088px;top:78px}

/* hero */
.hero{left:0;top:132px;width:1200px;height:608px;background:linear-gradient(120deg,#1d3f7e 0%,#3f68ad 45%,#7f9fd2 75%,#b9c9e3 100%);overflow:hidden}
.hero-cargo{left:590px;top:0;width:610px;height:608px;background:linear-gradient(160deg,rgba(226,178,120,0) 0%,rgba(198,148,96,.55) 60%,rgba(160,120,80,.35) 100%)}
.hero-frame{left:0;top:0}
.hero-title{left:89px;top:319px;width:499px;height:65px;border:4px solid #fff;border-radius:32px;background:var(--blue);color:#fff;font-family:"Roboto",Arial,sans-serif;font-weight:700;font-size:36px;display:flex;align-items:center;justify-content:center;letter-spacing:1px;white-space:nowrap}
.hero-text{left:80px;top:420px;width:520px;text-align:center;color:#fff;font-weight:700;font-size:25px;line-height:36px}
.hero-btn{left:252px;top:540px;width:199px;height:50px;background:#fff;color:var(--blue-dark);font-family:"Roboto",Arial,sans-serif;font-size:20px;display:flex;align-items:center;justify-content:center;letter-spacing:1px}

/* about */
.about-frame{left:310px;top:886px;width:240px;height:240px;border:22px solid #e6e6e6}
.about-photo{left:89px;top:787px;width:410px;height:307px;background:linear-gradient(135deg,#c9a878,#8a7a66 50%,#4d5a72)}
.about-tab{left:576px;top:782px;width:535px;height:58px;background:var(--blue);color:#fff;font-family:"Roboto",Arial,sans-serif;font-weight:700;font-size:24px;padding-left:76px;display:flex;align-items:center;border-top-right-radius:8px}
.about-tab::before{content:"";position:absolute;left:-14px;top:0;border-style:solid;border-width:0 14px 58px 0;border-color:transparent var(--blue-dark) transparent transparent}
.about-text{left:629px;top:858px;width:482px;font-size:17px;line-height:29px;color:var(--muted)}
.btn{background:var(--blue);color:#fff;font-family:"Roboto",Arial,sans-serif;font-weight:500;font-size:17px;display:flex;align-items:center;justify-content:center;white-space:nowrap}
.about-btn{left:629px;top:1080px;width:170px;height:48px}

/* services */
.services{left:0;top:1195px;width:1200px;height:533px;background:var(--blue)}
.services-title{left:84px;top:1214px;color:#fff;font-family:"Roboto",Arial,sans-serif;font-weight:700;font-size:24px}
.services-title::after{content:"";display:block;width:110px;height:2px;background:#fff;margin-top:6px}
.services-lead{left:84px;top:1266px;width:490px;color:#fff;font-size:15px;line-height:22px}
.svc{left:84px;width:485px;height:78px;background:var(--blue-soft);display:flex;align-items:center}
.svc-icon{width:78px;height:78px;display:flex;align-items:center;justify-content:center;border-right:2px solid rgba(255,255,255,.7)}
.svc-body{padding-left:26px;color:#fff;white-space:nowrap}
.svc-name{font-family:"Roboto",Arial,sans-serif;font-weight:700;font-size:15px;margin-bottom:6px}
.svc-desc{font-size:13px}
.svc-photo{left:581px;top:1195px;width:530px;height:365px;background:linear-gradient(180deg,#1a1c24 0%,#2e4a80 40%,#b98d5e 75%,#6c5a44 100%)}
.play{left:806px;top:1328px}
.help{left:581px;top:1560px;width:530px;height:168px;background:#f6f6f6;padding:20px 22px}
.help-title{font-family:"Roboto",Arial,sans-serif;font-weight:700;font-size:18px;margin-bottom:14px}
.help-text{font-size:16px;line-height:26px;color:var(--muted)}

/* solutions */
.sol-title{left:0;top:1782px;width:1200px;text-align:center;font-family:"Roboto",Arial,sans-serif;font-weight:500;font-size:30px}
.sol-rule{left:565px;top:1832px;width:70px;height:3px;background:#e09a4d}
.card{top:1901px;width:314px;height:228px}
.card-fill{width:100%;height:100%}
.card-label{position:absolute;left:18px;bottom:20px;height:42px;background:rgba(50,50,50,.85);color:#fff;font-family:"Roboto",Arial,sans-serif;font-size:15px;display:flex;align-items:center;padding:0 12px;gap:24px;letter-spacing:.3px;white-space:nowrap}
.card-go{width:44px;height:28px;background:var(--blue);display:flex;align-items:center;justify-content:center}

/* news */
.news-bg{left:0;top:2203px;width:1200px;height:521px;background:var(--grey-bg)}
.news-title{left:89px;top:2240px;font-family:"Roboto",Arial,sans-serif;font-weight:500;font-size:28px}
.news-rule{left:89px;top:2290px;width:1022px;height:1px;background:#ddd}
.news-all{left:943px;top:2237px;width:168px;height:36px;font-size:13px}
.post{top:2342px;width:310px;height:310px;background:#fff}
.post-photo{width:100%;height:195px}
.post-date{position:absolute;left:0;top:0;width:50px;height:58px;background:#2c2c2c;color:#fff;text-align:center;font-family:"Roboto",Arial,sans-serif;font-weight:700;font-size:22px;padding-top:4px;line-height:24px}
.post-date small{display:block;font-size:11px;font-weight:400}
.post-head{padding:26px 20px 0;font-family:"Roboto",Arial,sans-serif;font-weight:500;font-size:14px;line-height:19px}
.post-meta{padding:14px 20px 0;font-size:13px;font-style:italic;color:#777}
.callback{left:797px;top:2342px;width:314px;height:310px;background:var(--panel);color:#fff;padding:24px 26px}
.callback h3{font-family:"Roboto",Arial,sans-serif;font-weight:700;font-size:22px;white-space:nowrap}
.callback h3::after{content:"";display:block;width:100%;height:1px;background:#666;margin-top:14px}
.callback p{font-size:15px;line-height:21px;margin-top:20px}
.field{margin-top:28px;width:262px;height:48px;background:#fff;color:#999;font-style:italic;font-size:14px;padding-left:14px;display:flex;align-items:center}
.submit{margin-top:30px;width:156px;height:48px}

/* map */
.map{left:0;top:2724px;width:1200px;height:475px;background:linear-gradient(135deg,#d7e6c8 0%,#eef0e8 35%,#f3f1ea 60%,#e9e4d6 100%)}

/* footer */
.footer{left:0;top:3199px;width:1200px;height:310px;background:var(--foot)}
.contact-bar{left:0;top:3199px;width:1200px;height:94px;display:flex;align-items:center;padding-left:89px;font-size:15px;color:var(--foot-text);white-space:nowrap;border-bottom:1px solid #555}
.cbox{width:44px;height:32px;border:1px solid #777;display:flex;align-items:center;justify-content:center;margin:0 34px 0 22px;flex:none}
.foot-about{left:89px;top:3312px;width:400px;font-size:14.5px;line-height:26px;color:var(--foot-text)}
.foot-links{top:3310px;list-style:none;font-size:15px;line-height:26.5px;color:var(--foot-text);white-space:nowrap}
.foot-links li::before{content:"";display:inline-block;width:8px;height:8px;background:var(--blue-soft);margin-right:14px;transform:rotate(45deg)}
.news-sign{left:797px;top:3312px;color:var(--foot-text)}
.news-sign h4{font-family:"Roboto",Arial,sans-serif;font-weight:500;font-size:19px;white-space:nowrap}
.news-sign .field{margin-top:16px;width:316px;height:44px}
.news-sign .btn{margin-top:10px;width:140px;height:42px;background:#1f78c8;font-size:15px}
.bottom{left:0;top:3509px;width:1200px;height:91px;background:var(--foot-dark);color:#ddd;text-align:center;font-size:13px;padding-top:18px}
.socials{display:flex;justify-content:center;gap:8px;margin-bottom:10px}
.socials span{width:26px;height:26px;border-radius:50%;background:var(--blue)}
</style>
</head>
<body>

<header>
  <div class="abs topbar">
    <span><svg width="16" height="16" viewBox="0 0 16 16"><path d="M3 1l3 3-2 2c1 2 3 4 5 5l2-2 3 3-2 3C6 15 1 10 1 3z" fill="#fff"/></svg>+1-555-014-2200</span>
    <span><svg width="18" height="14" viewBox="0 0 18 14"><rect width="18" height="14" fill="#fff"/><path d="M0 0l9 7 9-7" stroke="#4d72b8" fill="none" stroke-width="1.5"/></svg>hello@northgate.example</span>
    <span>Login &nbsp;|&nbsp; Register</span>
  </div>
  <div class="abs brand"><div class="brand-dot"></div><div class="brand-name">NORTHGATE</div></div>
  <nav class="abs nav"><span class="active">HOME</span><span>ABOUT US</span><span>SERVICES</span><span>IT SOLUTIONS</span><span>NEWS</span><span>CONTACT US</span></nav>
  <svg class="abs search" width="22" height="22" viewBox="0 0 22 22"><circle cx="9" cy="9" r="7" stroke="#4d72b8" stroke-width="3" fill="none"/><path d="M14 14l6 6" stroke="#4d72b8" stroke-width="3"/></svg>
</header>

<section class="abs hero" role="img" aria-label="Port with cargo ships, aircraft and globe; warehouse worker leaning on stacked boxes on a pallet">
  <div class="abs hero-cargo"></div>
  <svg class="abs hero-frame" width="1200" height="608" viewBox="0 0 1200 608">
    <path d="M0 80 L340 -60 L700 300 L340 660 L0 470" stroke="#fff" stroke-width="18" fill="none"/>
    <path d="M20 20 L340 0 L640 300 L340 600" stroke="#fff" stroke-width="4" fill="none" opacity=".8"/>
  </svg>
</section>
<div class="abs hero-title">NORTHGATE LOGISTICS</div>
<p class="abs hero-text">Our warehouse facility may prove to be one of the most valuable extensions of your company’s operations</p>
<div class="abs hero-btn">READ MORE</div>

<section>
  <div class="abs about-frame"></div>
  <div class="abs about-photo" role="img" aria-label="Business team standing in a warehouse"></div>
  <div class="abs about-tab">WHO WE ARE</div>
  <p class="abs about-text">Our company was founded in 2012 but our team is seasoned, with a combined 75 years of experience. Northgate Logistics offers a complete logistics solution. With services dedicated to the changing economic environment.<br>Services to our customers include, same day delivery, trucking and van service, warehouse &amp; storage,</p>
  <div class="abs btn about-btn">READ MORE &gt;&gt;</div>
</section>

<section>
  <div class="abs services"></div>
  <h2 class="abs services-title">OUR SERVICES</h2>
  <p class="abs services-lead">It is a long established fact that a reader will be distracted by the readable content of a page</p>
  <div class="abs svc" style="top:1327px"><div class="svc-icon"><svg width="44" height="30" viewBox="0 0 44 30"><rect x="1" y="3" width="26" height="18" fill="none" stroke="#f0b070" stroke-width="2"/><path d="M27 9h9l6 7v5H27z" fill="none" stroke="#f0b070" stroke-width="2"/><circle cx="9" cy="25" r="3.5" fill="#f0b070"/><circle cx="34" cy="25" r="3.5" fill="#f0b070"/></svg></div><div class="svc-body"><div class="svc-name">TRUCK AND VAN SERVICES</div><div class="svc-desc">Trucking, vehicle and ground transportation include: &nbsp;&gt;&gt;</div></div></div>
  <div class="abs svc" style="top:1424px"><div class="svc-icon"><svg width="36" height="36" viewBox="0 0 36 36"><g stroke="#fff" stroke-width="2"><path d="M18 18L6 6M18 18L30 6M18 18L6 30M18 18L30 30"/></g><g fill="#fff"><circle cx="18" cy="18" r="5"/><circle cx="6" cy="6" r="4"/><circle cx="30" cy="6" r="4"/><circle cx="6" cy="30" r="4"/><circle cx="30" cy="30" r="4"/></g></svg></div><div class="svc-body"><div class="svc-name">DISTRIBUTION AND POOL SERIVES</div><div class="svc-desc">Pool Distribution is the distribution of product to nu &nbsp;&gt;&gt;</div></div></div>
  <div class="abs svc" style="top:1531px"><div class="svc-icon"><svg width="36" height="38" viewBox="0 0 36 38"><circle cx="18" cy="5" r="4" fill="#fff"/><path d="M18 10l-6 10h8l-4 16M18 10l8 10" stroke="#fff" stroke-width="3" fill="none"/><rect x="22" y="20" width="12" height="10" fill="#fff"/></svg></div><div class="svc-body"><div class="svc-name">SAME DAY DELIVERY SERVICES</div><div class="svc-desc">Regardless of the specifics of your needs, NORTHGATE &nbsp;&gt;&gt;</div></div></div>
  <div class="abs svc" style="top:1628px"><div class="svc-icon"><svg width="38" height="38" viewBox="0 0 38 38"><circle cx="19" cy="19" r="17" fill="#fff"/><circle cx="19" cy="19" r="10" fill="#6b8cc9"/><rect x="4" y="16" width="5" height="9" fill="#f0b070"/><rect x="29" y="16" width="5" height="9" fill="#f0b070"/></svg></div><div class="svc-body"><div class="svc-name">DEDICATED DELIVERY SERVICES</div><div class="svc-desc">Regardless of the specifics of your needs, NORTHGATE &nbsp;&gt;&gt;</div></div></div>
  <div class="abs svc-photo" role="img" aria-label="Workers loading boxes from a truck at a dock"></div>
  <svg class="abs play" width="80" height="80" viewBox="0 0 80 80"><circle cx="40" cy="40" r="38" fill="#4d72b8"/><path d="M32 24l22 16-22 16z" fill="#fff"/></svg>
  <div class="abs help"><div class="help-title">WE HELP YOUR BUSINESS</div><p class="help-text">Contrary to popular belief, Lorem Ipsum is not simply random text. It has roots in a piece of classical Latin literature from 45 BC, making it over 2000 years old</p></div>
</section>

<section>
  <h2 class="abs sol-title">WE OFFER A COMPLETE LOGISTICS SOLUTIONS</h2>
  <div class="abs sol-rule"></div>
  <div class="abs card" style="left:84px"><div class="card-fill" role="img" aria-label="Forklift inside a warehouse" style="background:linear-gradient(135deg,#a8c0de,#4d6f9e 60%,#2d3f5e)"></div><div class="card-label">VISIBILITY ACCOUNTING<span class="card-go"><svg width="14" height="14" viewBox="0 0 14 14"><circle cx="7" cy="7" r="7" fill="#fff"/><path d="M5 4l3 3-3 3" stroke="#4d72b8" stroke-width="2" fill="none"/></svg></span></div></div>
  <div class="abs card" style="left:432px"><div class="card-fill" role="img" aria-label="Hand holding a phone showing order tracking" style="background:linear-gradient(135deg,#3a2e26,#8a6a4e 55%,#c9a784)"></div><div class="card-label">MINUTE TRACKING<span class="card-go"><svg width="14" height="14" viewBox="0 0 14 14"><circle cx="7" cy="7" r="7" fill="#fff"/><path d="M5 4l3 3-3 3" stroke="#4d72b8" stroke-width="2" fill="none"/></svg></span></div></div>
  <div class="abs card" style="left:797px"><div class="card-fill" role="img" aria-label="Team meeting around a table seen from above" style="background:linear-gradient(135deg,#cfd3d8,#6f7d90 55%,#3c4656)"></div><div class="card-label">PROJECT MANAGEMENT<span class="card-go"><svg width="14" height="14" viewBox="0 0 14 14"><circle cx="7" cy="7" r="7" fill="#fff"/><path d="M5 4l3 3-3 3" stroke="#4d72b8" stroke-width="2" fill="none"/></svg></span></div></div>
</section>

<section>
  <div class="abs news-bg"></div>
  <h2 class="abs news-title">LATEST NEWS</h2>
  <div class="abs btn news-all">VIEW ALL ARTICLES +</div>
  <div class="abs news-rule"></div>
  <article class="abs post" style="left:89px"><div class="post-photo" role="img" aria-label="Worker checking stock on warehouse shelves" style="background:linear-gradient(135deg,#c25a3a,#d9a070 45%,#5c6f92)"></div><div class="post-date">12<small>APR</small></div><div class="post-head">LOREN IPSUM DOLAR SIT AMET CONSICLET SIT LOREN IPSUM</div><div class="post-meta">Mara Ellison / 2 Comments</div></article>
  <article class="abs post" style="left:444px"><div class="post-photo" role="img" aria-label="Woman with a tablet beside parcels" style="background:linear-gradient(135deg,#7f8fa8,#d0b28a 50%,#a07a52)"></div><div class="post-date">14<small>MAY</small></div><div class="post-head">LOREN IPSUM DOLAR SIT AMET CONSICLET SIT LOREN IPSUM</div><div class="post-meta">Mara Ellison / 2 Comments</div></article>
  <div class="abs callback"><h3>REQUEST A CALL BACK</h3><p>loren ipsum dolar sit amet consilet loren ipsum dolar</p><div class="field">enter your phone no</div><div class="btn submit">SUBMIT</div></div>
</section>

<div class="abs map" role="img" aria-label="City street map with location pins"></div>

<footer>
  <div class="abs footer"></div>
  <div class="abs contact-bar">
    <span>Have any Questions ?</span><span class="cbox"><svg width="16" height="14" viewBox="0 0 16 14"><path d="M1 13C2 6 6 4 11 4V1l4 5-4 5V8C7 8 4 9 1 13z" fill="#9ab"/></svg></span>
    <span>hello@northgate.example</span><span class="cbox"><svg width="18" height="12" viewBox="0 0 18 12"><rect width="18" height="12" fill="#9ab"/></svg></span>
    <span>+1-555-019-8800</span><span class="cbox"><svg width="16" height="16" viewBox="0 0 16 16"><path d="M3 1l3 3-2 2c1 2 3 4 5 5l2-2 3 3-2 3C6 15 1 10 1 3z" fill="#9ab"/></svg></span>
    <span>48 Harbor Row, Portland</span><span class="cbox"><svg width="12" height="16" viewBox="0 0 12 16"><path d="M6 16S0 9 0 6a6 6 0 0112 0c0 3-6 10-6 10z" fill="#9ab"/></svg></span>
  </div>
  <p class="abs foot-about">Our warehouse facility may prove to be one of the most valuable extensions of your company’s operations. With a secure warehouse conveniently located in central New England to supplement your firm’s storage and distribution needs.</p>
  <ul class="abs foot-links" style="left:511px"><li>Home</li><li>About Us</li><li>Services</li><li>Solutions</li><li>Blog</li><li>Contact Us</li></ul>
  <ul class="abs foot-links" style="left:636px"><li>Home</li><li>About Us</li><li>Services</li><li>Solutions</li><li>Blog</li><li>Contact Us</li></ul>
  <div class="abs news-sign"><h4>SUBSCRIBE OUR NEWSLETTER</h4><div class="field">enter your e-mail address</div><div class="btn">SUBSCRIBE</div></div>
  <div class="abs bottom"><div class="socials"><span></span><span></span><span></span><span></span></div>Copyright2017.All Right Reserved</div>
</footer>

</body>
</html>
```